Small business services company needs a flyer designed

We need a flyer designed for a small building services company who has multiple roles ie- Roof, gutter and pressure cleaning, small building maintenance and garden cleanups. The company is based in Far North Queensland (Australia) where it is a tropical climate with lots of trees and green areas.

I want the colours to be based on the Logo and business card colours which will be added.

The flyer will need to be changeable so I can create monthly specials ie- Roof Cleaning Special, Gutter Cleaning Special or Pressure Cleaning special.

The roles of the business will be as stated on the attached business card.
Updates

Good evening all designers, please find below an update for you all, I hope it may answer some questions you have.

'd like the flyer to be DL size and at present I don't have any photo's. But i'd be happy for you to source some from google. The pictures I'd like would be of gutter cleaning from a ladder, pressure washing roofs & driveways with the large round "flat surface cleaners". Possibly have split pictures of the pressure cleaning to show before and after. 
Far North Queensland is a very tropical environment that has lots of palm trees and rain forest. The climate is usually 30+ degrees C. Incorporating those colours with the logo colours I'd like. 

Hello all designers.

I have just uploaded some of my own job pictures. There is a before and an after picture. If you source any other pictures, I'd like to see a flat surface/ spindeck cleaner in operation, either on a roof or a driveway.

My goal is for a single sided flyer with all the details from my business card to be on the flyer. 

Please remember the climate in my area is very tropical and usually 30+ degrees C. Never cold or snowing. So please have pictures to reflect.

Thanks for the designs.
Regards,Glenn

Reason: hi all designers. I have extended the deadline by 3 days to accommodate all the designers who have only recently accepted the craft hive invites. I have had a lot of declines and want the best designs I can choice from. This is no reflection of the calibre of the designs I have already received. I look forward to seeing all the updates and new designs. Regards, Glenn

Target Market(s)

Home owners who take pride in the street appeal of their homes, or to add value to their selling price when a house goes on the sales market.

Industry/Entity Type

Building

```html
<!DOCTYPE html>
<html lang="en">
<head>
<meta charset="utf-8">
<title>Upreach Flyer</title>
<link rel="stylesheet" href="https://fonts.googleapis.com/css2?family=Roboto+Condensed:wght@700&family=Source+Sans+3:wght@400;600&family=Arimo:wght@700&display=swap">
<style>
:root{
  --teal:#17a697;
  --teal-dark:#128a7d;
  --navy:#2b3a9a;
  --white:#ffffff;
  --ink:#0d0d0d;
  --stage:#3a3a3a;
  --stage-light:#5a5a5a;
  --photo-a:#6f7a73;
  --photo-b:#a9adb0;
  --badge-a:#8f9694;
  --badge-b:#5e6664;
}
*{margin:0;padding:0;box-sizing:border-box}
html,body{width:1200px;height:999px;overflow:hidden}
body{background:radial-gradient(ellipse at center,var(--stage-light) 0%,var(--stage) 75%);position:relative;font-family:"Source Sans 3",sans-serif}
.flyer{position:absolute;left:378px;top:38px;width:436px;height:923px;background:var(--teal);overflow:hidden}
.brand-band{position:absolute;left:0;top:23px;width:436px;height:141px;background:var(--white)}
.brand-name{position:absolute;left:48px;top:28px;font-family:"Roboto Condensed",sans-serif;font-weight:700;font-size:56px;color:var(--navy);letter-spacing:1px;line-height:1}
.brand-mark{position:absolute;left:310px;top:34px;width:54px;height:54px;border-radius:50%;background:var(--navy)}
.brand-tagline{position:absolute;left:48px;top:96px;font-family:"Roboto Condensed",sans-serif;font-weight:700;font-size:10px;color:var(--navy);letter-spacing:.3px}
.brand-call{position:absolute;left:100px;top:112px;font-family:"Roboto Condensed",sans-serif;font-weight:700;font-size:13px;color:var(--teal-dark);letter-spacing:.5px}
.hero-photo{position:absolute;left:0;top:170px;width:436px;height:380px;background:linear-gradient(100deg,var(--photo-a) 0%,var(--photo-a) 40%,var(--photo-b) 100%)}
.wave{position:absolute;left:0;top:430px;width:436px;height:140px}
.headline{position:absolute;left:26px;top:500px;font-family:"Roboto Condensed",sans-serif;font-weight:700;font-size:60px;color:var(--white);line-height:1;white-space:nowrap}
.subline{position:absolute;left:26px;top:572px;font-size:23px;line-height:29px;color:var(--white)}
.badge{position:absolute;left:268px;top:514px;width:156px;height:156px}
.badge-text{position:absolute;left:268px;top:536px;width:156px;text-align:center;color:var(--white);line-height:1.15}
.badge-text .pct,.badge-text .word{font-family:"Roboto Condensed",sans-serif;font-weight:700;display:block}
.badge-text .pct{font-size:26px}
.badge-text .word{font-size:20px}
.badge-text .small{font-size:13px;display:block;line-height:18px}
.service-title{position:absolute;left:21px;top:652px;font-family:"Roboto Condensed",sans-serif;font-weight:700;font-size:32px;color:var(--white)}
.service-list{position:absolute;left:21px;top:694px;list-style:none;font-size:20px;line-height:25px;color:var(--white)}
.clientele{position:absolute;left:21px;top:779px;font-size:17.5px;font-weight:600;color:var(--white)}
.phone-band{position:absolute;left:0;top:820px;width:436px;height:54px;background:var(--white);text-align:center;font-family:"Arimo",sans-serif;font-weight:700;font-size:42px;line-height:54px;color:var(--ink);letter-spacing:1px}
.email{position:absolute;left:0;top:874px;width:436px;text-align:center;font-size:20px;line-height:28px;color:var(--white)}
</style>
</head>
<body>
<main class="flyer">
  <header class="brand-band">
    <div class="brand-name">UPREACH</div>
    <div class="brand-mark"></div>
    <div class="brand-tagline">ROOF, GUTTER &amp; PRESSURE CLEANING SERVICES</div>
    <div class="brand-call">CALL 0491 570 266</div>
  </header>

  <div class="hero-photo" role="img" aria-label="Photo of a worker cleaning a gutter along a grey shingle roof beside a green hedge"></div>

  <svg class="wave" viewBox="0 0 436 140" preserveAspectRatio="none" aria-hidden="true">
    <path d="M0 32 C90 14 190 30 280 70 C340 96 390 110 436 104 L436 140 L0 140 Z" fill="#4a4a4a"/>
    <path d="M0 40 C100 20 200 40 290 84 C350 112 395 124 436 118 L436 140 L0 140 Z" fill="var(--teal)"/>
  </svg>

  <h1 class="headline">UPREACH</h1>
  <p class="subline">Roof, Gutter &amp; Pressure<br>Cleaning Service</p>

  <svg class="badge" viewBox="-80 -80 160 160" aria-hidden="true">
    <defs>
      <radialGradient id="badgeFill" cx="50%" cy="40%" r="60%">
        <stop offset="0%" stop-color="var(--badge-a)"/>
        <stop offset="100%" stop-color="var(--badge-b)"/>
      </radialGradient>
    </defs>
    <polygon fill="url(#badgeFill)" stroke="#fff" stroke-width="2.5" points="78,0 67.2,10.6 74.2,24.1 60.6,30.9 63.1,45.9 48.1,48.1 45.9,63.1 30.9,60.6 24.1,74.2 10.6,67.2 0,78 -10.6,67.2 -24.1,74.2 -30.9,60.6 -45.9,63.1 -48.1,48.1 -63.1,45.9 -60.6,30.9 -74.2,24.1 -67.2,10.6 -78,0 -67.2,-10.6 -74.2,-24.1 -60.6,-30.9 -63.1,-45.9 -48.1,-48.1 -45.9,-63.1 -30.9,-60.6 -24.1,-74.2 -10.6,-67.2 0,-78 10.6,-67.2 24.1,-74.2 30.9,-60.6 45.9,-63.1 48.1,-48.1 63.1,-45.9 60.6,-30.9 74.2,-24.1 67.2,-10.6"/>
  </svg>
  <div class="badge-text">
    <span class="pct">10%</span>
    <span class="word">Discount</span>
    <span class="small">for Emergency<br>Services<br>Defence &amp;<br>Seniors</span>
  </div>

  <h2 class="service-title">Gutter Cleaning</h2>
  <ul class="service-list">
    <li>Pressure Cleaning-Roof’s, Driveways ets</li>
    <li>Minor Roof, Gutter &amp; Building Maintenance</li>
    <li>Garden Waste Removal &amp; Complex Cleanup</li>
  </ul>
  <p class="clientele">Residential, Commercial &amp; Body Corporate Jobs</p>

  <div class="phone-band">0491 570 266</div>
  <div class="email">roofcleaning@skylinemail.com.au</div>
</main>
</body>
</html>
```